Web Design Project - Valdora Homes

We would like you to refine our web layouts for a (1) homepage and (2) a product page (see attached files for reference).

The client is a swiss construction company, that designs, builds and sells standardized and tailored-made residential houses.

His logo is old, but not up for redesign. The only way to salvage it, is to incorporate its yellow color (as highlight) to the overall design, so as to create some brand awareness.

REQUIREMENTS FOR THE HOMEPAGE:
1. telephone number over menu
2. logo + menu with 6 categories
3. slider for showing various house types (for pics, see attachments)
4. "AKTUELL" card with yellow color (to show his most actual projects) and a strong Call For Action (what in German would be: KONTAKT AUFNEHMEN)
5. a yellow stripe for his company's slogan (Ihr Partner für individuelle und normierte Wohnbauten)
6. A left coloumn with
(a) two picture-holders under the title REFERENZEN
(b) the three supporting logos of ENVALO, VOLTARIS and VB KLIMABAU VERBUND (can be downloaded as pngs)
7. A right column with 6 headlines + texts of 3 lines each
8. a footer with the adress info

REQUIREMENTS FOR PRODUKT PAGE:
1. slider for pictures
2. info box with Call For Action for particular House-types
3. thumbnail pics under the slider for additional images of any particular house type
4. Left-side: name of house type and picture
5. Right-side: Header and blindtext for house description
6. three placeholders for 3 floor plans
Updates

NB No coding necessary. An imaginative, fresh design along the layout requirements will do.
Thanx to all

To all those who had probs with the downloading of the attached files:
we've posted a new Zip.
Have a look!
thankx

Thanks to everyone who participated.
We will be showing a selection of your designs to the client within the next couple of days.
We'll get back to you, as soon as possible.

Industry/Entity Type

Construction

Requirements
Must have
• - slider
- info box with call for action
- thumbnail pictures
- fresh look based on colors, design of elements (slider, info box), font selection

```html
<!DOCTYPE html>
<html lang="de">
<head>
<meta charset="utf-8">
<title>Valdora Homes</title>
<link href="https://fonts.googleapis.com/css2?family=Arimo:wght@400;700&family=Teko:wght@500;600&display=swap" rel="stylesheet">
<style>
:root{
  --page:#ececec;
  --dark:#222222;
  --dark-2:#111111;
  --yellow:#ffc709;
  --yellow-dark:#c79a00;
  --panel:#e8e8e8;
  --text:#333333;
  --muted:#555555;
  --white:#ffffff;
  --sky:#4a6fb0;
  --grass:#4f7a33;
}
*{margin:0;padding:0;box-sizing:border-box}
html,body{width:1200px;height:1200px;overflow:hidden}
body{
  background:linear-gradient(#f7f7f7 0,#f0f0f0 400px,var(--page) 400px,#e4e4e4 1200px);
  font-family:"Arimo",Arial,sans-serif;color:var(--text);position:relative;
}
.brand{position:absolute;left:152px;top:30px;display:flex;align-items:center;gap:8px}
.brand-mark{width:14px;height:36px;background:var(--yellow)}
.brand-name{font-size:22px;font-weight:700;color:var(--dark)}
.phone{position:absolute;left:900px;top:38px;display:flex;gap:18px;align-items:center}
.phone-icon{width:32px;height:32px;border-radius:4px;background:var(--dark);display:flex;align-items:center;justify-content:center}
.phone-label{font-size:14px;font-weight:700;color:var(--dark);line-height:17px}
.phone-number{font-size:14px;color:var(--dark);line-height:17px}
.sheet{position:absolute;left:130px;top:100px;width:940px;height:1080px;background:var(--white);box-shadow:0 0 6px rgba(0,0,0,.2);border-radius:4px 4px 0 0}
.nav{height:40px;background:linear-gradient(#2a2a2a,var(--dark-2));border-radius:4px 4px 0 0;position:relative}
.nav a{position:absolute;top:14px;color:var(--white);font-size:12px;font-weight:700;text-decoration:none;letter-spacing:.1px;line-height:14px}
.nav a.active::after{content:"";position:absolute;left:50%;bottom:-12px;margin-left:-4px;border:4px solid transparent;border-bottom-color:var(--white)}
.slider{position:absolute;left:10px;top:50px;width:450px;height:250px;background:var(--dark)}
.slide{width:450px;height:220px;background:linear-gradient(180deg,var(--sky) 0,#8fb0d8 45%,#e8e8e8 60%,var(--grass) 100%)}
.slider-controls{position:absolute;left:20px;bottom:9px;display:flex;gap:5px;align-items:center}
.dot{width:8px;height:8px;background:var(--white)}
.dot.on{background:var(--yellow)}
.news{position:absolute;left:460px;top:50px;width:470px;height:250px;background:var(--panel)}
.news-fold{position:absolute;right:0;top:0;width:0;height:0;border-left:16px solid #cfcfcf;border-bottom:16px solid transparent}
.news-title{position:absolute;left:51px;top:17px;font-size:16px;font-weight:700;letter-spacing:.4px;color:var(--dark)}
.news-rule{position:absolute;left:140px;width:280px;height:3px;background:var(--dark)}
.news-list{position:absolute;left:140px;top:43px;width:280px;list-style:none}
.news-list li{height:26.7px;line-height:26px;border-bottom:1px dotted #b8b8b8;font-size:14px;color:var(--text);padding-left:22px;position:relative}
.news-list li:last-child{border-bottom:0}
.news-list li svg{position:absolute;left:0;top:7px}
.cta{position:absolute;left:139px;top:205px;width:162px;height:32px;border:1px solid #bdbdbd;border-radius:4px;background:linear-gradient(#f4f4f4,#dcdcdc);font-size:12.5px;font-weight:700;color:#333;text-align:center;line-height:30px;letter-spacing:.3px}
.slogan{position:absolute;left:120px;top:420px;width:960px;height:40px;background:var(--yellow)}
.slogan::before,.slogan::after{content:"";position:absolute;bottom:-7px;border-top:7px solid var(--yellow-dark)}
.slogan::before{left:0;border-left:10px solid transparent}
.slogan::after{right:0;border-right:10px solid transparent}
.slogan p{font-family:"Teko",sans-serif;font-weight:600;font-size:21px;color:var(--dark);line-height:44px;padding-left:40px;letter-spacing:.3px}
.refs{position:absolute;left:160px;top:482px}
.refs h2,.features h2{font-size:18px;font-weight:400;color:var(--dark);line-height:22px}
.ref-photo{width:260px;height:160px;border-radius:8px;border:3px solid #f2f2f2;box-shadow:0 0 2px rgba(0,0,0,.3);margin-top:6px}
.ref-photo.a{background:linear-gradient(180deg,var(--sky) 0,#9bb8dc 50%,var(--grass) 100%)}
.ref-photo.b{margin-top:20px;background:linear-gradient(180deg,#b8cde0 0,#e6eaee 55%,#6d8e4a 100%)}
.partners{position:absolute;left:158px;top:870px}
.badge{background:#d9d9d9;border-radius:4px}
.features{position:absolute;left:450px;top:482px;width:585px}
.features h2{margin-bottom:2px}
.features p{font-size:11.8px;line-height:14.6px;color:var(--muted);margin-bottom:12px}
.footer{position:absolute;left:130px;top:1098px;width:940px;height:82px;background:var(--dark);color:#eee;font-size:12.5px;line-height:21px}
.footer div{position:absolute;top:13px}
</style>
</head>
<body>
<div class="brand"><span class="brand-mark"></span><span class="brand-name">Valdora Homes</span></div>
<div class="phone">
  <div class="phone-icon"><svg width="18" height="18" viewBox="0 0 24 24"><path fill="#fff" d="M6.6 10.8a15 15 0 0 0 6.6 6.6l2.2-2.2c.3-.3.7-.4 1-.2 1.1.4 2.3.6 3.6.6.6 0 1 .4 1 1V20c0 .6-.4 1-1 1A17 17 0 0 1 3 4c0-.6.4-1 1-1h3.5c.6 0 1 .4 1 1 0 1.3.2 2.5.6 3.6.1.3 0 .7-.2 1z"/></svg></div>
  <div><div class="phone-label">PHONE</div><div class="phone-number">071 555 20 40</div></div>
</div>

<div class="sheet">
  <nav class="nav">
    <a class="active" style="left:28px">HOME</a><a style="left:98px">HÄUSER</a><a style="left:181px">RENOVATIONEN</a><a style="left:311px">REFERENZEN</a><a style="left:426px">ÜBER UNS</a><a style="left:522px">KONTAKT</a>
  </nav>
  <div class="slider">
    <div class="slide" role="img" aria-label="Foto eines weissen Einfamilienhauses mit rotem Dach"></div>
    <div class="slider-controls">
      <svg width="10" height="12" viewBox="0 0 10 12"><path d="M7 1 2 6l5 5" stroke="#fff" stroke-width="2" fill="none"/></svg>
      <span class="dot on"></span><span class="dot"></span><span class="dot"></span><span class="dot"></span><span class="dot"></span>
      <svg width="10" height="12" viewBox="0 0 10 12"><path d="m3 1 5 5-5 5" stroke="#fff" stroke-width="2" fill="none"/></svg>
    </div>
  </div>
  <div class="news">
    <div class="news-fold"></div>
    <div class="news-title">AKTUELL</div>
    <div class="news-rule" style="top:28px"></div>
    <ul class="news-list">
      <li><svg width="14" height="14" viewBox="0 0 14 14"><path d="M7 1 13 7 7 13 1 7z" fill="none" stroke="#ffc709" stroke-width="1.5"/><path d="m5 4 3 3-3 3" stroke="#ffc709" stroke-width="1.5" fill="none"/></svg>Bauland in Brunnau, TG</li>
      <li><svg width="14" height="14" viewBox="0 0 14 14"><path d="M7 1 13 7 7 13 1 7z" fill="none" stroke="#ffc709" stroke-width="1.5"/><path d="m5 4 3 3-3 3" stroke="#ffc709" stroke-width="1.5" fill="none"/></svg>Bauland in Felsheim, TG</li>
      <li><svg width="14" height="14" viewBox="0 0 14 14"><path d="M7 1 13 7 7 13 1 7z" fill="none" stroke="#ffc709" stroke-width="1.5"/><path d="m5 4 3 3-3 3" stroke="#ffc709" stroke-width="1.5" fill="none"/></svg>EFN in Rosental, TG</li>
      <li><svg width="14" height="14" viewBox="0 0 14 14"><path d="M7 1 13 7 7 13 1 7z" fill="none" stroke="#ffc709" stroke-width="1.5"/><path d="m5 4 3 3-3 3" stroke="#ffc709" stroke-width="1.5" fill="none"/></svg>EFN in Auwil, TG</li>
      <li><svg width="14" height="14" viewBox="0 0 14 14"><path d="M7 1 13 7 7 13 1 7z" fill="none" stroke="#ffc709" stroke-width="1.5"/><path d="m5 4 3 3-3 3" stroke="#ffc709" stroke-width="1.5" fill="none"/></svg>Wohnungen in Talwil, TG</li>
    </ul>
    <div class="news-rule" style="top:188px"></div>
    <div class="cta">KONTAKT AUFNEHMEN</div>
  </div>
</div>

<div class="slogan"><p>Ihr Partner für individuelle und normierte Wohnbauten</p></div>

<section class="refs">
  <h2>Referenzen</h2>
  <div class="ref-photo a" role="img" aria-label="Referenzfoto: weisses Einfamilienhaus mit rotem Dach"></div>
  <div class="ref-photo b" role="img" aria-label="Referenzfoto: weisses Haus mit grauem Dach und Wintergarten"></div>
</section>
<div class="partners">
  <div class="badge" role="img" aria-label="Partnerabzeichen ENVALO" style="width:128px;height:60px"></div>
  <div class="badge" role="img" aria-label="Partnerabzeichen VOLTARIS" style="width:164px;height:34px;margin-top:18px"></div>
  <div class="badge" role="img" aria-label="Partnerabzeichen VB KLIMABAU VERBUND" style="width:256px;height:36px;margin-top:18px"></div>
</div>

<section class="features">
  <h2>Beratung und Betreuung</h2>
  <p>Lorem ipsum dolor sit amet, consectetur adipiscing elit. Vestibulum sed convallis metus. Proin pulvinar, tortor eget gravida faucibus, justo enim tempor lacus, ut ultricies nibh nisi vel lectus. Vivamus quis justo dolor, sit amet ultrices turpis.</p>
  <h2>Auf Ihre Wünsche</h2>
  <p>Aenean convallis lorem metus. Integer a eros vitae nisi rhoncus aliquet. Sed pellentesque eleifend erat, id pellentesque sem lobortis vitae. Aliquam erat volutpat. Nunc hendrerit nunc tortor. In sodales nisi non tortor sagittis luctus. Nullam commodo lobortis ante, vel auctor urna facilisis quis.</p>
  <h2>Zusammenarbeit</h2>
  <p>Maecenas pharetra nunc dui. Donec lacinia elit non nisi sodales eleifend. Donec vehicula, nisi quis tincidunt consectetur, metus sapien volutpat ante, vitae blandit arcu urna sit amet ligula. Nunc condimentum, lectus rhoncus viverra sollicitudin, nulla quam sagittis purus, non rutrum lorem sapien sit amet eros.</p>
  <h2>Für jedes Bugdet</h2>
  <p>Vivamus sodales orci nec nulla pharetra volutpat. Fusce libero neque, sagittis vel pharetra eget, viverra a nibh. Praesent mauris lectus, mollis id elementum eu, sollicitudin in arcu. Nulla lacinia tortor nec elit euismod a malesuada purus molestie. Aenean id sem libero, et eleifend sapien.</p>
  <h2>Umweltfreundlich</h2>
  <p>Aliquam volutpat massa quis turpis malesuada interdum. Donec pulvinar ligula in erat fringilla condimentum. Etiam vitae quam ipsum, ac pretium purus. Cum sociis natoque penatibus et magnis dis parturient montes, nascetur ridiculus mus. Sed nec egestas massa. Vivamus euismod aliquam commodo.</p>
  <h2>Kundenzufriedenheit</h2>
  <p>Lorem ipsum dolor sit amet, consectetur adipiscing elit. Vestibulum sed convallis metus. Proin pulvinar, tortor eget gravida faucibus, justo enim tempor lacus, ut ultricies nibh nisi vel lectus. Vivamus quis justo dolor, sit amet ultrices turpis. Donec ante enim, gravida vel pharetra vitae, volutpat in urna.</p>
</section>

<footer class="footer">
  <div style="left:30px">Valdora Homes GmbH<br>Fam. Berner</div>
  <div style="left:240px">Lindenweg 12<br>CH-8999 Talwil</div>
  <div style="left:480px">Tel. 071 555 20 40<br>Fax. 071 555 20 41</div>
  <div style="left:720px">info@valdora-homes.ch</div>
</footer>
</body>
</html>
```